New Company Business Card design

Looking for a corporate looking business card utilising my new logo design - the logo i would like embossed as one option and flat as another - simplistic but stylish - less is more - we are an import export business launching into the market - i would like a couple of options as main background - Grey or Black

```html
<!DOCTYPE html>
<html lang="en">
<head>
<meta charset="utf-8">
<title>Meridian Trade Partners – Business Card</title>
<link href="https://fonts.googleapis.com/css2?family=Open+Sans:wght@400;600&display=swap" rel="stylesheet">
<style>
  :root {
    --card-bg: #282f37;
    --page-bg: #ffffff;
    --brand-blue: #1f7dc6;
    --text-grey: #a3a8ad;
    --mark-grey: #6f7378;
  }
  html, body {
    margin: 0;
    padding: 0;
    width: 1200px;
    height: 1200px;
    overflow: hidden;
    background: var(--page-bg);
    font-family: "Open Sans", sans-serif;
  }
  .sheet {
    position: relative;
    width: 1200px;
    height: 1200px;
  }
  .card {
    position: absolute;
    left: 0;
    width: 1200px;
    background: var(--card-bg);
  }
  .card--front { top: 0; height: 584px; }
  .card--back { top: 619px; height: 581px; }

  .person {
    position: absolute;
    left: 44px;
    top: 262px;
  }
  .person__name {
    margin: 0;
    color: var(--brand-blue);
    font-size: 33px;
    font-weight: 600;
    letter-spacing: 1px;
    line-height: 1;
  }
  .person__role {
    margin: 14px 0 0;
    color: var(--text-grey);
    font-size: 22px;
    font-weight: 400;
    line-height: 1;
  }

  .contact {
    position: absolute;
    left: 40px;
    top: 398px;
    margin: 0;
    padding: 0;
    list-style: none;
  }
  .contact__item {
    display: flex;
    align-items: center;
    height: 37px;
    color: var(--text-grey);
    font-size: 25px;
    letter-spacing: 1.6px;
  }
  .contact__icon {
    width: 26px;
    height: 26px;
    margin-right: 20px;
    flex: none;
  }

  .brand {
    position: absolute;
    display: flex;
    align-items: center;
    gap: 18px;
    color: var(--brand-blue);
    font-weight: 600;
    letter-spacing: 2px;
    white-space: nowrap;
  }
  .brand__dot {
    border-radius: 50%;
    background: var(--brand-blue);
    flex: none;
  }
  .brand--front {
    right: 70px;
    top: 222px;
    font-size: 30px;
  }
  .brand--front .brand__dot { width: 34px; height: 34px; }
  .brand--back {
    left: 0;
    right: 0;
    justify-content: center;
    top: 250px;
    font-size: 44px;
  }
  .brand--back .brand__dot { width: 50px; height: 50px; }

  .address {
    position: absolute;
    right: 70px;
    top: 474px;
    margin: 0;
    text-align: right;
    color: var(--text-grey);
    font-size: 24px;
    font-style: normal;
    line-height: 32px;
    letter-spacing: 0.5px;
  }
</style>
</head>
<body>
<main class="sheet">
  <section class="card card--front">
    <div class="person">
      <h1 class="person__name">JHON SMITH</h1>
      <p class="person__role">MANAGER</p>
    </div>

    <ul class="contact">
      <li class="contact__item">
        <svg class="contact__icon" viewBox="0 0 24 24" fill="none" stroke="var(--brand-blue)" stroke-width="2" stroke-linecap="round" stroke-linejoin="round">
          <path d="M5 3h3l2 5-2.5 1.5a11 11 0 0 0 7 7L16 14l5 2v3a2 2 0 0 1-2 2A17 17 0 0 1 3 5a2 2 0 0 1 2-2z"/>
          <path d="M14 3a7 7 0 0 1 7 7M14 7a3 3 0 0 1 3 3"/>
        </svg>
        +1111 2222 3333 4444
      </li>
      <li class="contact__item">
        <svg class="contact__icon" viewBox="0 0 24 24" fill="none" stroke="var(--brand-blue)" stroke-width="1.8">
          <rect x="6" y="2" width="12" height="20" rx="2"/>
          <circle cx="12" cy="18.5" r="0.8" fill="var(--brand-blue)"/>
        </svg>
        +1111 2222 3333 4444
      </li>
      <li class="contact__item">
        <svg class="contact__icon" viewBox="0 0 24 24" fill="none" stroke="var(--brand-blue)" stroke-width="1.8" stroke-linejoin="round">
          <rect x="2" y="5" width="20" height="14" rx="1.5"/>
          <path d="M2 6l10 7 10-7"/>
        </svg>
        info@yourmail.com
      </li>
      <li class="contact__item">
        <svg class="contact__icon" viewBox="0 0 24 24" fill="none" stroke="var(--brand-blue)" stroke-width="1.8">
          <circle cx="12" cy="12" r="9.5"/>
          <ellipse cx="12" cy="12" rx="4" ry="9.5"/>
          <path d="M2.5 12h19M4 7h16M4 17h16"/>
        </svg>
        www.yourwebsite.com
      </li>
    </ul>

    <div class="brand brand--front">
      <span class="brand__dot"></span>
      <span class="brand__name">MERIDIAN TRADE PARTNERS</span>
    </div>

    <address class="address">
      1450 Harbor Point Dr, Suite 210,<br>
      Norfolk, VA 23510
    </address>
  </section>

  <section class="card card--back">
    <div class="brand brand--back">
      <span class="brand__dot"></span>
      <span class="brand__name">MERIDIAN TRADE PARTNERS</span>
    </div>
  </section>
</main>
</body>
</html>
```